Byaruhanga & Odongo Advocates website

An interactive professional law firm website fully synchronized with social media pages.

Target Market(s)

Corporations and professionals

Industry/Entity Type

Professional Service

Number of Pages Required

5+ page

Font styles to use
Sans Serif

Colors

Designer to choose colors to be used in the design.

```html
<!DOCTYPE html>
<html lang="en">
<head>
<meta charset="utf-8">
<title>Byaruhanga &amp; Odongo Advocates</title>
<link href="https://fonts.googleapis.com/css2?family=Cinzel:wght@400;700&family=Open+Sans:wght@400;600;700&display=swap" rel="stylesheet">
<style>
:root{
  --red:#9b1c2c;
  --red-dark:#7d1422;
  --ink:#2a2a2a;
  --char:#333335;
  --night:#232323;
  --grey:#f0f0f0;
  --line:#dddddd;
  --text:#555;
  --white:#fff;
}
*{box-sizing:border-box;margin:0;padding:0}
html,body{width:1200px;height:5184px;overflow:hidden}
body{font-family:"Open Sans",Arial,sans-serif;color:var(--text);background:var(--white);font-size:13px;line-height:1.6;position:relative}
h1,h2,h3{font-family:"Cinzel",Georgia,serif;font-weight:700;letter-spacing:1px}
.wrap{width:940px;margin:0 auto;position:relative}
section{position:relative}
.sec-title{text-align:center;color:var(--ink);font-size:22px;text-transform:uppercase}
.sec-title::after{content:"";display:block;width:50px;height:2px;background:var(--red);margin:10px auto 0}
.btn{display:inline-block;background:var(--red);color:var(--white);font-size:10px;font-weight:700;text-transform:uppercase;letter-spacing:1px;padding:8px 18px}
.btn.ghost{background:transparent;border:1px solid var(--white)}

/* top bar */
.topbar{height:40px;background:var(--night);color:#bbb;font-size:11px}
.topbar .wrap{display:flex;justify-content:space-between;align-items:center;height:40px}
.topbar span{display:flex;align-items:center;gap:6px}

/* nav */
.nav{height:72px;background:var(--red)}
.nav .wrap{display:flex;justify-content:space-between;align-items:center;height:72px}
.brand{display:flex;align-items:center;gap:8px;color:var(--white);font-size:15px;font-weight:700;white-space:nowrap}
.brand i{display:block;width:12px;height:12px;background:var(--white)}
.menu{display:flex;gap:20px;list-style:none;color:var(--white);font-size:12px}

/* hero */
.hero{height:480px;background:linear-gradient(180deg,#c9c9c9 0%,#9a9a9a 45%,#5c5c5c 100%)}
.hero-photo{position:absolute;inset:0}
.hero-card{position:absolute;left:50%;transform:translateX(-50%);top:336px;width:460px;background:rgba(35,35,35,.92);text-align:center;padding:18px 20px 18px;z-index:1}
.hero-card h1{background:var(--red);color:var(--white);font-size:19px;padding:10px;margin:0 -20px}
.hero-card p{color:#ddd;font-size:10px;letter-spacing:2px;text-transform:uppercase;margin:8px 0 12px}
.side-tab{position:absolute;right:0;top:130px;width:30px;height:160px;background:var(--red-dark);color:var(--white);font-size:10px;writing-mode:vertical-rl;text-align:center;letter-spacing:2px;padding-top:14px}
.social-rail{position:absolute;left:0;top:800px;display:flex;flex-direction:column;gap:2px;z-index:2}
.social-rail i{display:block;width:22px;height:22px;background:var(--red)}
.social-rail i:nth-child(2){background:#555}

/* who */
.who{height:520px;padding-top:112px}
.who .lead{width:640px;margin:24px auto 0;text-align:center;font-size:12px}
.who-cols{display:flex;justify-content:space-between;margin-top:30px}
.vm{width:380px}
.vm h3{font-family:"Open Sans",sans-serif;color:var(--ink);font-size:15px;letter-spacing:0;margin-top:14px}
.vm p{font-size:12px}
.who-img{width:470px;height:200px;background:linear-gradient(135deg,#e9e9e9,#bfc4c8 60%,#8e959b)}

/* history */
.history{height:400px;background:linear-gradient(90deg,#3b3b3b,#555 50%,#3b3b3b)}
.history .panel{position:absolute;left:130px;right:130px;top:0;bottom:0;background:var(--red);text-align:center;color:var(--white);padding:70px 70px 0}
.history .sec-title{color:var(--white)}
.history .sec-title::after{background:var(--white)}
.history p{font-size:12px;margin:22px 0 26px;color:#f2dede}

/* practice */
.practice{height:488px;padding-top:90px}
.cards{display:flex;justify-content:space-between;margin-top:50px}
.card{width:290px;height:230px;background:var(--char);color:var(--white);text-align:center;padding:28px 24px}
.card.feature{background:var(--red)}
.card svg{width:42px;height:42px}
.card h3{font-size:14px;margin:10px 0 8px}
.card p{font-size:10px;color:#ccc;line-height:1.5}
.card .more{font-size:10px;font-weight:700;margin-top:12px;display:block}

/* stats */
.stats{height:392px;background:var(--char)}
.stats-photo{position:absolute;left:0;top:0;width:640px;height:392px;background:linear-gradient(160deg,#b9bdc1,#7d8288 50%,#5a5e63);clip-path:polygon(0 0,100% 0,80% 100%,0 100%)}
.stat-grid{position:absolute;left:660px;top:80px;width:400px;display:grid;grid-template-columns:1fr 1fr;row-gap:40px;color:var(--white);text-align:center}
.stat svg{width:30px;height:30px}
.stat b{display:block;font-size:18px;font-family:"Cinzel",serif}
.stat small{font-size:10px;letter-spacing:1px;text-transform:uppercase;color:#ccc}

/* team */
.team{height:448px;padding-top:50px}
.team-row{display:flex;justify-content:space-between;margin-top:44px}
.member{width:220px;text-align:center}
.member .photo{height:220px;background:linear-gradient(180deg,#6b6f74,#2f3236)}
.member.active .photo{background:linear-gradient(180deg,#b8283a,#7d1422);position:relative}
.member .icons{position:absolute;left:8px;top:30px;display:flex;flex-direction:column;gap:3px}
.member .icons i{display:block;width:16px;height:16px;background:var(--white);opacity:.85}
.member h4{font-size:12px;color:var(--ink);margin-top:12px;letter-spacing:1px;text-transform:uppercase;font-family:"Cinzel",serif}
.member small{font-size:10px;color:var(--red)}
.arrow{position:absolute;color:#999;font-size:22px}

/* reviews */
.reviews{height:500px;padding-top:60px}
.avatar{width:80px;height:80px;border-radius:50%;border:3px solid var(--red);background:linear-gradient(180deg,#7a7e83,#3a3d41);margin:24px auto 0;position:relative;z-index:1}
.quote{width:560px;margin:-20px auto 0;background:var(--grey);text-align:center;padding:40px 40px 20px;font-size:11px}
.quote b{display:block;margin-top:10px;font-size:10px;color:var(--ink);letter-spacing:1px}

/* clients */
.clients{padding-top:10px}
.group-title{text-align:center;color:var(--red);font-size:13px;font-weight:700}
.group-title::after{content:"";display:block;width:130px;height:1px;background:var(--red);margin:6px auto 0}
.logo-grid{display:flex;flex-wrap:wrap;justify-content:center;gap:28px 24px;width:800px;margin:26px auto 40px}
.logo-grid.five{width:660px}
.client{width:110px;height:110px;border:1px solid var(--line);box-shadow:0 2px 4px rgba(0,0,0,.08);display:flex;align-items:center;justify-content:center;gap:5px;font-size:11px;font-weight:700;color:var(--char)}
.client i{width:9px;height:9px;background:var(--red);display:block}

/* consultation */
.consult{position:absolute;left:0;top:4440px;width:1200px;height:520px;background:var(--night);padding-top:70px}
.consult .sec-title{color:var(--white);font-weight:400}
.form{width:620px;margin:40px auto 0;display:grid;grid-template-columns:1fr 1fr;gap:16px}
.field{height:36px;border:1px solid #555;color:#888;font-size:11px;padding:9px 12px}
.field.msg{grid-column:1/3;height:120px}
.form .btn{grid-column:1/3;justify-self:center;padding:9px 34px}

/* footer */
.footer{position:absolute;left:0;top:4960px;width:1200px;height:224px;background:#1b1b1b;color:#999;font-size:10px}
.footer .wrap{display:flex;gap:60px;padding-top:56px}
.footer .brand{align-self:flex-start}
.footer p{line-height:1.7}
</style>
</head>
<body>

<div class="topbar"><div class="wrap">
  <span><svg width="10" height="12" viewBox="0 0 10 12"><path d="M5 0a4 4 0 0 0-4 4c0 3 4 8 4 8s4-5 4-8a4 4 0 0 0-4-4z" fill="#9b1c2c"/></svg>Plot 24 Nile Crescent, 2nd Floor, Kampala, Uganda</span>
  <span><svg width="11" height="11" viewBox="0 0 11 11"><path d="M2 0l2 2-1 2c1 2 2 3 4 4l2-1 2 2-2 2C4 11 0 7 0 2z" fill="#9b1c2c"/></svg>+256 700 000 111</span>
</div></div>

<nav class="nav"><div class="wrap">
  <div class="brand"><i></i>Byaruhanga &amp; Odongo</div>
  <ul class="menu"><li>Home</li><li>Our History</li><li>Who We Are</li><li>How We Work</li><li>Practice Areas</li><li>Our Clients</li><li>Our Professionals</li><li>Contact Us</li></ul>
</div></nav>

<section class="hero">
  <div class="hero-photo" role="img" aria-label="Team photograph of the firm's advocates standing before stone columns"></div>
  <div class="side-tab">CONSULT</div>
  <div class="hero-card">
    <h1>Byaruhanga &amp; Odongo Advocates</h1>
    <p>Construction &amp; Commercial Litigation</p>
    <span class="btn">Book your appointment</span>
  </div>
</section>

<div class="social-rail"><i></i><i></i><i></i><i></i></div>

<section class="who"><div class="wrap">
  <h2 class="sec-title">Who We Are</h2>
  <p class="lead">Byaruhanga &amp; Odongo Advocates is a specialist commercial law firm in Uganda focusing on commercial litigation, construction law and arbitration. We have remained a trusted name for over two decades and we continue to grow among the best firms in the region.</p>
  <div class="who-cols">
    <div class="vm">
      <h3>Vision</h3>
      <p>To be the firm of choice in our niche practice areas of commercial law.</p>
      <h3>Mission</h3>
      <p>To provide experienced and focused commercial legal, construction law and arbitration with efficiency, integrity and client satisfaction.</p>
    </div>
    <div class="who-img" role="img" aria-label="Firm signage beside a modern office building"></div>
  </div>
</div></section>

<section class="history">
  <div class="panel">
    <h2 class="sec-title">Our History</h2>
    <p>In the year the firm was founded by a small team of advocates, it set out to provide dependable commercial legal services. Over the years the firm has grown into a leading practice with partners and associates serving corporations, government agencies and individuals across East Africa, building lasting relationships with clients in Kenya, Rwanda, Tanzania and beyond.</p>
    <span class="btn ghost">Read More</span>
  </div>
</section>

<section class="practice"><div class="wrap">
  <h2 class="sec-title">Practice Areas</h2>
  <div class="cards">
    <div class="card">
      <svg viewBox="0 0 42 42" fill="none" stroke="#fff" stroke-width="2"><path d="M4 16L21 6l17 10z"/><path d="M9 18v14M17 18v14M25 18v14M33 18v14M4 36h34"/></svg>
      <h3>Commercial Litigation</h3>
      <p>We represent clients in complex commercial disputes before courts and tribunals, with clear strategy and focused advocacy.</p>
      <span class="more">READ MORE &rsaquo;</span>
    </div>
    <div class="card feature">
      <svg viewBox="0 0 42 42" fill="none" stroke="#fff" stroke-width="2"><path d="M21 6v30M10 36h22M8 12h26"/><path d="M8 12l-5 12h10zM34 12l-5 12h10z"/></svg>
      <h3>Arbitration</h3>
      <p>We guide parties through domestic and international arbitration, resolving disputes efficiently and with discretion.</p>
      <span class="more">READ MORE &rsaquo;</span>
    </div>
    <div class="card">
      <svg viewBox="0 0 42 42" fill="none" stroke="#fff" stroke-width="2"><path d="M8 14l10-10 8 8-10 10z"/><path d="M20 16l16 16"/><path d="M4 38h22"/></svg>
      <h3>Construction Law</h3>
      <p>We advise contractors, developers and employers on contracts, claims and disputes across every stage of a project.</p>
      <span class="more">READ MORE &rsaquo;</span>
    </div>
  </div>
</div></section>

<section class="stats">
  <div class="stats-photo" role="img" aria-label="Aerial view of a city highway interchange"></div>
  <div class="stat-grid">
    <div class="stat"><svg viewBox="0 0 30 30" fill="#c62a3d"><circle cx="10" cy="9" r="5"/><circle cx="21" cy="9" r="5"/><path d="M1 28c0-7 4-11 9-11s9 4 9 11zM14 28c0-7 3-11 7-11s8 4 8 11z"/></svg><b>5</b><small>Partners</small></div>
    <div class="stat"><svg viewBox="0 0 30 30" fill="#c62a3d"><circle cx="15" cy="9" r="6"/><path d="M4 28c0-8 5-12 11-12s11 4 11 12z"/></svg><b>20+</b><small>Advocates</small></div>
    <div class="stat"><svg viewBox="0 0 30 30" fill="none" stroke="#c62a3d" stroke-width="2.5"><rect x="3" y="5" width="24" height="22"/><path d="M3 11h24M9 2v6M21 2v6"/></svg><b>60+</b><small>Years of combined experience</small></div>
    <div class="stat"><svg viewBox="0 0 30 30" fill="none" stroke="#c62a3d" stroke-width="2.5"><rect x="3" y="8" width="24" height="18"/><path d="M11 8V4h8v4"/></svg><b>350+</b><small>Cases handled</small></div>
  </div>
</section>

<section class="team"><div class="wrap">
  <h2 class="sec-title">Meet Our Team</h2>
  <span class="arrow" style="left:-40px;top:200px">&lsaquo;</span>
  <span class="arrow" style="right:-40px;top:200px">&rsaquo;</span>
  <div class="team-row">
    <div class="member active"><div class="photo" role="img" aria-label="Portrait of the managing partner"><div class="icons"><i></i><i></i><i></i></div></div><h4>Peter M. Byaruhanga</h4><small>Managing Partner</small></div>
    <div class="member"><div class="photo" role="img" aria-label="Portrait of a senior partner"></div><h4>Daniel O. Odongo</h4><small>Senior Partner</small></div>
    <div class="member"><div class="photo" role="img" aria-label="Portrait of the head of litigation"></div><h4>Samuel Atwine</h4><small>Head of Litigation</small></div>
    <div class="member"><div class="photo" role="img" aria-label="Portrait of a partner"></div><h4>Nicholas Tumusiime</h4><small>Partner</small></div>
  </div>
</div></section>

<section class="reviews"><div class="wrap">
  <h2 class="sec-title">Our Client Reviews</h2>
  <div class="avatar" role="img" aria-label="Client portrait"></div>
  <div class="quote">The team handled our dispute with great care and clear advice from the first meeting to the final award. Their knowledge of construction contracts saved us time and cost, and they kept us informed at every step. We would gladly work with them again on any commercial matter.<b>GRACE NAMUTEBI</b></div>
</div></section>

<section class="clients">
  <div class="group-title">Corporate Advisory</div>
  <div class="logo-grid five">
    <div class="client"><i></i>Solvo</div><div class="client">Altura Capital</div><div class="client"><i></i>Pinera</div><div class="client">Nuvia</div><div class="client"><i></i>Kestrel</div>
    <div class="client">Orvane</div><div class="client"><i></i>Tembo</div><div class="client">Lakeline</div><div class="client"><i></i>Amara</div><div class="client">Bisoro</div>
  </div>
  <div class="group-title">Construction &amp; Arbitration</div>
  <div class="logo-grid">
    <div class="client"><i></i>Stonex</div><div class="client">Rokta</div><div class="client">Ridgeline</div><div class="client"><i></i>Umbra</div><div class="client">Corvane</div><div class="client"><i></i>Kalira</div>
    <div class="client">Mertoz</div><div class="client"><i></i>Savo</div>
  </div>
  <div class="group-title">Commercial Litigation and Transactions</div>
  <div class="logo-grid">
    <div class="client"><i></i>Dalex</div><div class="client">Tigra</div><div class="client"><i></i>Rubico</div><div class="client">Helvo</div><div class="client">Packora</div><div class="client"><i></i>Zenta</div>
    <div class="client"><i></i>Greenfold</div>
  </div>
</section>

<section class="consult">
  <h2 class="sec-title">Request Your Consultation</h2>
  <div class="form">
    <div class="field">Name</div><div class="field">Email</div>
    <div class="field">Phone</div><div class="field">Are you a new client?</div>
    <div class="field msg">Message</div>
    <span class="btn">Send</span>
  </div>
</section>

<footer class="footer"><div class="wrap">
  <div class="brand"><i></i>Byaruhanga &amp; Odongo</div>
  <p>Head Office: Byaruhanga &amp; Odongo<br>Plot 24 Nile Crescent<br>2nd Floor, Crest House<br>P.O. Box 1200<br>Kampala, Uganda</p>
  <p>+256 700 000 111<br>+256 700 000 222<br>info@byaruhangaodongo.example<br>www.byaruhangaodongo.example</p>
</div></footer>

</body>
</html>
```